Book Cover Design - Business/Self-Help Book

Book cover design for a business/self-help book. The title of the book is "OTTER Compass - Seven Quiet Habits of Steady Growth" It should also have "Unlock the Nine Hidden Keys Behind Lasting Momentum" as a subtitle somewhere.

Please see the website for an idea of the logo and sub-words: http://www.ottercompassbook.com

Book size will be 8.5" x 5.25"
Author info: Marlo Quindt

If your design includes a shark on the cover, it MUST be a hammerhead shark. Logo is attached.

I would like to stick with a red or orange theme like on the website but am open to any color idea. I like brighter colors and want the book to stand out and be attractive. If it's white, the wording and logo should be a bright color.

The back cover will just be preview text and selling points. It could have a picture in the background but will not have any pictures of the author.

If you include a spine design, please put the hammerhead logo on the spine.

Target Market(s)

Young Entrepreneurs and Business Professionals

Industry/Entity Type

Business

Requirements
Must have
• The hammerhead shark logo
Nice to have
• Look at the website - http://www.ottercompassbook.com
• It would be nice to have the six words throughout the cover similar to how it shows on the website cover picture.
Should not have
• Even though it caters to a younger crowd, it should not be cartoonish or child-like. Want a more serious and modern feel. Not too cluttered, i want the title to stand out and the shark to stand out.

```html
<!DOCTYPE html>
<html lang="en">
<head>
<meta charset="utf-8">
<title>OTTER Compass – Seven Quiet Habits of Steady Growth</title>
<link rel="stylesheet" href="https://fonts.googleapis.com/css2?family=Oswald:wght@400;600;700&display=swap">
<style>
  :root {
    --page-bg: #f4f4f4;
    --cover-white: #ffffff;
    --band-orange: #f08a3c;
    --band-red: #e2472a;
    --band-deep: #c9321f;
    --title-orange: #ea5a2c;
    --text-white: #ffffff;
    --creature-grey: #444444;
  }
  * { margin: 0; padding: 0; box-sizing: border-box; }
  html, body {
    width: 912px; height: 1200px; overflow: hidden;
    background: var(--page-bg);
    font-family: "Oswald", "Arial Narrow", sans-serif;
  }
  .cover {
    position: absolute; left: 156px; top: 90px;
    width: 600px; height: 1020px;
    background: var(--cover-white);
    overflow: hidden;
    box-shadow: 0 10px 30px rgba(0,0,0,0.18);
  }
  .band { position: absolute; left: 0; width: 600px; }
  .band--top { top: 0; height: 218px; }
  .band--bottom { bottom: 0; height: 124px; }
  .band svg { display: block; width: 100%; height: 100%; }

  .brand {
    position: absolute; top: 46px; left: 0; width: 100%;
    display: flex; justify-content: center; align-items: center; gap: 14px;
    color: var(--text-white);
    font-weight: 600; font-size: 48px; line-height: 1; letter-spacing: 1px; text-transform: uppercase;
  }
  .brand__dot {
    width: 14px; height: 14px; border-radius: 50%; background: var(--text-white);
  }
  .pillars {
    position: absolute; top: 150px; left: 0; width: 100%;
    text-align: center; color: var(--text-white);
    font-weight: 400; font-size: 15px; letter-spacing: 1.5px; text-transform: uppercase;
    word-spacing: 3px;
  }

  .creature {
    position: absolute; left: 400px; top: 240px; width: 170px; height: 520px;
    background: linear-gradient(180deg, #4a4a4a, #3a3a3a);
    border-radius: 48% 48% 40% 40% / 20% 20% 60% 60%;
  }

  .title {
    position: absolute; left: 38px; top: 250px; width: 350px;
    color: var(--title-orange);
    font-weight: 700; font-size: 78px; line-height: 1.04;
    letter-spacing: 3px; text-transform: uppercase;
  }
  .subtitle {
    position: absolute; right: 28px; top: 790px;
    color: var(--band-red);
    font-weight: 700; font-size: 26px; line-height: 1.1;
    text-align: right; text-transform: uppercase;
  }
  .author {
    position: absolute; left: 32px; bottom: 30px;
    color: var(--text-white);
    font-weight: 600; font-size: 22px; letter-spacing: 1px; text-transform: uppercase;
  }
</style>
</head>
<body>
  <main class="cover">
    <div class="band band--top">
      <svg viewBox="0 0 600 218" preserveAspectRatio="none" aria-hidden="true">
        <defs>
          <linearGradient id="topWash" x1="0" y1="0" x2="1" y2="1">
            <stop offset="0" stop-color="var(--band-orange)"/>
            <stop offset="0.55" stop-color="var(--band-red)"/>
            <stop offset="1" stop-color="var(--band-orange)"/>
          </linearGradient>
        </defs>
        <path fill="url(#topWash)" d="M0 0 H600 V186 C560 204 520 182 480 198 C430 214 390 190 340 204 C290 216 250 194 200 206 C150 216 110 192 60 202 C35 208 15 200 0 204 Z"/>
      </svg>
    </div>
    <div class="brand"><span class="brand__dot"></span>Otter Compass</div>
    <p class="pillars">Focus + Patience + Routine + Courage + Clarity + Trust</p>

    <div class="creature" role="img" aria-label="Dark grey hammerhead shark silhouette swimming diagonally"></div>

    <h1 class="title">Seven<br>Quiet<br>Habits of<br>Steady<br>Growth</h1>
    <p class="subtitle">Unlock the Nine Hidden<br>Keys Behind Lasting<br>Momentum</p>

    <div class="band band--bottom">
      <svg viewBox="0 0 600 124" preserveAspectRatio="none" aria-hidden="true">
        <defs>
          <linearGradient id="bottomWash" x1="0" y1="0" x2="1" y2="0">
            <stop offset="0" stop-color="var(--band-deep)"/>
            <stop offset="0.5" stop-color="var(--band-red)"/>
            <stop offset="1" stop-color="var(--band-orange)"/>
          </linearGradient>
        </defs>
        <path fill="url(#bottomWash)" d="M0 22 C40 12 80 30 130 20 C180 10 220 28 270 18 C320 8 370 26 420 14 C470 4 520 22 560 10 C580 6 592 8 600 8 V124 H0 Z"/>
      </svg>
    </div>
    <p class="author">Author: Marlo Quindt</p>
  </main>
</body>
</html>
```